A business card design for a dental office. We have Two doctors working here. We practice general de

I already have a logo designed for the office with the name and a slogan.
Now I need to create design for a business card using the same logo.
Details Needed on the front side of the card are :
Gregory L. Vanmerick, DDS
Daniel R Hoskett, DDS
418 Birchwood Lane
Portland, CT 06512
Phone : 860 555 0193
Fax : 860 555 0194
Website : WWW.BrightcrestDental.Com
Office hours by appointment
On the back side of the card need :
Appointment
Date....................Time...................
With....................................
If unable to keep your appointment, please give 24-48 hours notice in order to avoid broken appointment fee.

Industry/Entity Type

Dental Clinic

Contact Information for Business Card

Gregory L. Vanmerick, DDS
Daniel R Hoskett, DDS
418 Birchwood Lane
Portland, CT 06512
Phone : 860 555 0193
Fax : 860 555 0194
Appointment

Requirements
Must have
• Keep the Name and slogan on the logo on the front of the card. You can move them around the Logo and Name/Slogan of business (Vanmerick Family Dentistry/We give you reasons to smile) as you wish to get a feel of the design.
• Gregory L. Vanmerick, DDS
• Daniel R Hoskett, DDS
• 418 Birchwood Lane
• Portland, CT 06512
• Phone : 860 555 0193
• Fax : 860 555 0194
• WWW.BrightcrestDental.Com
• Keep these three groups above as they are together now in different areas of the front side.
• On the back side of the card need :
• Appointment
• Date....................Time...................
• With....................................
• If unable to keep your appointment, please give 24-48 hours notice in order to avoid broken appointment fee.

```html
<!DOCTYPE html>
<html lang="en">
<head>
<meta charset="utf-8">
<title>Vanmerick Family Dentistry – Business Card</title>
<link rel="stylesheet" href="https://fonts.googleapis.com/css2?family=Arimo:wght@400;700&family=Michroma&display=swap">
<style>
  :root {
    --ink: #111111;
    --paper: #f6f6f4;
    --stage: #e4e2de;
    --brand-blue: #1f5aa6;
    --deep-blue: #1d4f9c;
    --brand-red: #e0404e;
    --accent-red: #d8232f;
    --teal: #1ea886;
    --night: #060606;
    --icon-teal: #27b08f;
  }
  * { box-sizing: border-box; margin: 0; padding: 0; }
  html, body { width: 1200px; height: 892px; overflow: hidden; }
  body {
    background: var(--stage);
    font-family: "Arimo", Arial, sans-serif;
    position: relative;
  }
  .card {
    position: absolute;
    left: 260px;
    width: 680px;
    height: 388px;
    background: var(--paper);
    overflow: hidden;
    box-shadow: 0 6px 18px rgba(0,0,0,0.18);
  }
  .card-front { top: 40px; }
  .card-back { top: 464px; }
  .card-art { position: absolute; inset: 0; width: 100%; height: 100%; }

  /* front */
  .brand-mark {
    position: absolute; left: 140px; top: 22px;
    width: 92px; height: 92px; border-radius: 50%;
    background: #eef3f8; border: 3px solid var(--teal);
  }
  .brand-name {
    position: absolute; left: 250px; top: 50px;
    font-family: "Michroma", "Arimo", sans-serif;
    color: var(--brand-blue); font-size: 16px; letter-spacing: 0.5px;
    text-transform: uppercase; white-space: nowrap;
  }
  .brand-slogan {
    position: absolute; left: 250px; top: 82px; width: 360px;
    display: flex; align-items: center; gap: 10px;
    color: var(--accent-red); font-size: 9px; letter-spacing: 2px;
    text-transform: uppercase; white-space: nowrap;
  }
  .brand-slogan::before, .brand-slogan::after {
    content: ""; flex: 1; height: 1px; background: var(--accent-red);
  }
  .doctors { position: absolute; left: 34px; top: 188px; }
  .doctor-name {
    font-family: "Michroma", "Arimo", sans-serif;
    color: var(--brand-red); font-size: 16px; letter-spacing: 0.3px;
    text-transform: uppercase; white-space: nowrap; line-height: 1.15;
  }
  .doctor-title {
    color: var(--brand-red); font-size: 12px; margin-bottom: 8px;
    font-family: "Michroma", "Arimo", sans-serif;
  }
  .rule-h { position: absolute; left: 34px; top: 286px; width: 206px; height: 1.5px; background: var(--ink); }
  .rule-v { position: absolute; left: 240px; top: 274px; width: 1.5px; height: 100px; background: var(--ink); }
  .contacts { position: absolute; left: 254px; top: 280px; list-style: none; }
  .contacts li {
    display: flex; align-items: center; gap: 8px;
    font-size: 15px; color: var(--ink); line-height: 22px; white-space: nowrap;
  }
  .contact-icon { width: 13px; height: 13px; flex: none; }

  /* back */
  .appointment-title {
    position: absolute; left: 0; right: 0; top: 28px; text-align: center;
    font-family: "Michroma", "Arimo", sans-serif; font-weight: 700;
    color: #ffffff; font-size: 32px; letter-spacing: 2px; text-transform: uppercase;
  }
  .slot-list { position: absolute; left: 40px; top: 160px; list-style: none; }
  .slot {
    font-size: 23px; color: #222; margin-bottom: 22px; white-space: nowrap;
    letter-spacing: 0.3px;
  }
  .slot .leader { color: #333; letter-spacing: 0; }
  .notice {
    position: absolute; left: 40px; right: 40px; top: 334px;
    font-size: 12.5px; line-height: 1.4; color: #333; text-align: center;
  }
</style>
</head>
<body>

<section class="card card-front" aria-label="Business card front">
  <svg class="card-art" viewBox="0 0 680 388" aria-hidden="true">
    <path d="M0,0 H680 V180 L560,200 Q330,120 0,172 Z" fill="var(--night)"/>
    <path d="M0,176 Q330,128 515,212 Q580,260 600,388" fill="none" stroke="var(--brand-blue)" stroke-width="10"/>
    <polygon points="560,200 680,118 680,180" fill="var(--accent-red)"/>
    <polygon points="560,200 680,180 680,388 610,388" fill="var(--deep-blue)"/>
    <polygon points="495,208 560,200 588,318" fill="var(--teal)"/>
  </svg>
  <div class="brand-mark" role="img" aria-label="Vanmerick Family Dentistry emblem area"></div>
  <div class="brand-name">Vanmerick Family Dentistry</div>
  <div class="brand-slogan">We give you reasons to smile</div>

  <div class="doctors">
    <p class="doctor-name">Gregory L. Vanmerick</p>
    <p class="doctor-title">DDS</p>
    <p class="doctor-name">Daniel R Hoskett</p>
    <p class="doctor-title">DDS</p>
  </div>
  <div class="rule-h"></div>
  <div class="rule-v"></div>

  <ul class="contacts">
    <li>
      <svg class="contact-icon" viewBox="0 0 14 14" aria-label="Phone"><rect width="14" height="14" rx="3" fill="var(--icon-teal)"/><path d="M4,3 L6,3 L6.5,5.5 L5.5,6.3 Q6.5,8 7.7,8.5 L8.5,7.5 L11,8 L11,10 Q6,11 4,3 Z" fill="#fff"/></svg>
      860 555 0193
    </li>
    <li>
      <svg class="contact-icon" viewBox="0 0 14 14" aria-label="Fax"><rect width="14" height="14" rx="3" fill="var(--icon-teal)"/><rect x="3" y="6" width="8" height="5" fill="#fff"/><rect x="4.5" y="3" width="5" height="3" fill="#fff"/></svg>
      860 555 0194
    </li>
    <li>
      <svg class="contact-icon" viewBox="0 0 14 14" aria-label="Website"><rect width="14" height="14" rx="3" fill="var(--icon-teal)"/><circle cx="7" cy="7" r="4" fill="none" stroke="#fff" stroke-width="1.3"/><line x1="3" y1="7" x2="11" y2="7" stroke="#fff" stroke-width="1"/></svg>
      WWW.BrightcrestDental.Com
    </li>
    <li>
      <svg class="contact-icon" viewBox="0 0 14 14" aria-label="Address"><rect width="14" height="14" rx="3" fill="var(--icon-teal)"/><path d="M7,12 L4,7 A3.3,3.3 0 1 1 10,7 Z" fill="#fff"/><circle cx="7" cy="5.6" r="1.2" fill="var(--icon-teal)"/></svg>
      418 Birchwood Lane Portland, CT 06512
    </li>
  </ul>
</section>

<section class="card card-back" aria-label="Appointment card back">
  <svg class="card-art" viewBox="0 0 680 388" aria-hidden="true">
    <path d="M0,0 H680 V62 Q360,72 0,110 Z" fill="var(--deep-blue)"/>
    <path d="M0,110 Q360,72 680,62 V70 Q360,80 0,118 Z" fill="var(--accent-red)"/>
    <circle cx="190" cy="240" r="120" fill="#dfe6ee" opacity="0.55"/>
  </svg>
  <h2 class="appointment-title">Appointment</h2>
  <ul class="slot-list">
    <li class="slot">Date<span class="leader">....................</span>Time<span class="leader">..................</span>With<span class="leader">......................</span></li>
    <li class="slot">Date<span class="leader">....................</span>Time<span class="leader">..................</span>With<span class="leader">......................</span></li>
    <li class="slot">Date<span class="leader">....................</span>Time<span class="leader">..................</span>With<span class="leader">......................</span></li>
  </ul>
  <p class="notice">If unable to keep your appointment, please give 24-48 hours notice in order to avoid broken appointment fee.</p>
</section>

</body>
</html>
```